Beef cattle farm needs signs which can be seen from roadside

We would like submissions of artwork for a sign that will hang from a fence or gate and will be seen by passing cars.

Existing logo and branding theme for the company is attached.

Signage can be between 900mm x 400mm - 1200mm x 600mm

Industry/Entity Type

Farm

Requirements
Must have
• the Signs should have the following information:
• Company name: Bellwin Grazing Company
• Address: 184 Tilbury Creek Road
• Contact number: 0491 362 815
• email address: admin@bellwingrazingco.example.com.au
• - Logo and branding as per attached artwork

```html
<!DOCTYPE html>
<html lang="en">
<head>
<meta charset="utf-8">
<title>Bellwin Grazing Company – Roadside Sign</title>
<link rel="stylesheet" href="https://fonts.googleapis.com/css2?family=Open+Sans:wght@600;700&family=Montserrat:wght@500;600&display=swap">
<style>
  :root {
    --farm-green: #136a10;
    --ink-black: #111111;
    --sign-white: #ffffff;
    --backdrop: #e9e6e1;
  }
  html, body {
    margin: 0;
    padding: 0;
    width: 1200px;
    height: 1000px;
    overflow: hidden;
    background: var(--backdrop);
  }
  .canvas {
    position: relative;
    width: 1200px;
    height: 1000px;
  }
  .sign {
    position: absolute;
    left: 15px;
    top: 285px;
    width: 1170px;
    height: 520px;
    background: var(--sign-white);
    overflow: hidden;
    box-shadow: 0 3px 8px rgba(0,0,0,0.25);
    font-family: "Open Sans", Arial, sans-serif;
  }
  .sign__bands {
    position: absolute;
    inset: 0;
  }
  .sign__title {
    position: absolute;
    top: 2px;
    left: 0;
    width: 100%;
    text-align: center;
    margin: 0;
    color: var(--sign-white);
    font-weight: 700;
    font-size: 61px;
    letter-spacing: 0.5px;
    line-height: 72px;
  }
  .brand {
    position: absolute;
    left: 80px;
    top: 160px;
    width: 290px;
    text-align: center;
  }
  .brand__dot {
    display: block;
    width: 180px;
    height: 180px;
    margin: 0 auto 14px;
    border-radius: 50%;
    background: var(--farm-green);
  }
  .brand__name {
    font-family: "Montserrat", Arial, sans-serif;
    font-weight: 600;
    color: var(--farm-green);
    font-size: 25px;
    line-height: 32px;
    letter-spacing: 1px;
    margin: 0;
  }
  .contact {
    position: absolute;
    left: 440px;
    width: 710px;
    color: var(--farm-green);
    font-weight: 700;
    margin: 0;
  }
  .contact--phone {
    top: 170px;
    display: flex;
    align-items: center;
    justify-content: center;
    gap: 26px;
    font-size: 64px;
    line-height: 80px;
  }
  .contact--address {
    top: 295px;
    text-align: center;
    font-size: 50px;
    line-height: 64px;
  }
  .contact__icon {
    width: 50px;
    height: 86px;
  }
  .footer {
    position: absolute;
    left: 0;
    bottom: 0;
    width: 100%;
    height: 62px;
    display: flex;
    align-items: center;
    justify-content: center;
    gap: 44px;
    color: var(--sign-white);
    font-weight: 700;
    font-size: 34px;
    padding-right: 70px;
    box-sizing: border-box;
  }
  .footer__icon {
    width: 54px;
    height: 36px;
  }
</style>
</head>
<body>
<div class="canvas">
  <div class="sign">
    <svg class="sign__bands" viewBox="0 0 1170 520" preserveAspectRatio="none" aria-hidden="true">
      <!-- top band with swoosh -->
      <path d="M0 175 C 300 110, 700 75, 1170 72 L1170 62 C 700 62, 300 95, 0 150 Z" fill="var(--ink-black)"/>
      <path d="M0 0 H1170 V62 C 700 62, 300 95, 0 142 Z" fill="var(--farm-green)"/>
      <!-- bottom band with swoosh -->
      <path d="M620 462 C 850 440, 1050 410, 1170 388 L1170 410 C 1000 425, 820 445, 620 462 Z" fill="var(--ink-black)"/>
      <path d="M0 458 C 500 468, 900 445, 1170 415 V520 H0 Z" fill="var(--farm-green)"/>
    </svg>

    <h1 class="sign__title">BELLWIN GRAZING COMPANY</h1>

    <div class="brand">
      <span class="brand__dot"></span>
      <p class="brand__name">BELLWIN GRAZING COMPANY</p>
    </div>

    <p class="contact contact--phone">
      <svg class="contact__icon" viewBox="0 0 50 86" aria-hidden="true">
        <path d="M14 2 C6 4 2 12 2 24 C2 48 10 70 26 82 C30 85 36 84 40 80 L46 72 C48 69 47 66 44 64 L34 56 C31 54 28 55 26 58 L23 62 C16 54 12 40 13 28 L18 27 C21 26 23 24 23 20 L22 8 C22 4 19 1 14 2 Z" fill="var(--farm-green)"/>
      </svg>
      <span>0491 362 815</span>
    </p>

    <p class="contact contact--address">184 Tilbury Creek Road</p>

    <div class="footer">
      <svg class="footer__icon" viewBox="0 0 54 36" aria-hidden="true">
        <rect x="2" y="2" width="50" height="32" fill="none" stroke="var(--sign-white)" stroke-width="3"/>
        <path d="M2 2 L27 22 L52 2 M2 34 L21 17 M52 34 L33 17" fill="none" stroke="var(--sign-white)" stroke-width="3"/>
      </svg>
      <span>admin@bellwingrazingco.example.com.au</span>
    </div>
  </div>
</div>
</body>
</html>
```